Redesign of Business Cards to Update them!

We want a full overhaul of our business cards! We have a design that is almost 5 years old and it needs to be updated to be current

Address is 457 Calloway Court Suite B Fernvale CA 92417
PH: 9094417382
Tindlebox.com

Hours M-F 10AM-4PM
Sat and Sunday Closed

```html
<!DOCTYPE html>
<html lang="en">
<head>
<meta charset="utf-8">
<title>Tindlebox Business Cards</title>
<link href="https://fonts.googleapis.com/css2?family=Roboto:wght@400;500;900&display=swap" rel="stylesheet">
<style>
  :root {
    --canvas-bg: #ecebe8;
    --card-bg: #ffffff;
    --brand-red: #e8242b;
    --deep-red: #a8141c;
    --ink: #111111;
    --ink-soft: #222222;
    --card-shadow: rgba(0, 0, 0, 0.18);
  }
  * { box-sizing: border-box; margin: 0; padding: 0; }
  html, body {
    width: 1200px;
    height: 800px;
    overflow: hidden;
  }
  body {
    background: var(--canvas-bg);
    font-family: "Roboto", Arial, sans-serif;
    display: flex;
    align-items: center;
    justify-content: center;
    gap: 40px;
  }
  .card {
    position: relative;
    width: 540px;
    height: 309px;
    background: var(--card-bg);
    box-shadow: 0 10px 28px var(--card-shadow);
    overflow: hidden;
  }

  .halftone {
    position: absolute;
    top: 0;
    bottom: 0;
  }
  .halftone--front {
    right: 0;
    width: 60%;
    background: linear-gradient(100deg, rgba(255,255,255,0) 0%, rgba(232,36,43,0.15) 35%, rgba(232,36,43,0.55) 70%, var(--deep-red) 100%);
  }
  .halftone--back {
    left: 0;
    width: 66%;
    background: linear-gradient(90deg, var(--deep-red) 0%, var(--brand-red) 30%, rgba(232,36,43,0.35) 65%, rgba(255,255,255,0) 100%);
  }

  .brand {
    display: flex;
    align-items: center;
    gap: 10px;
  }
  .brand__dot {
    width: 26px;
    height: 26px;
    border-radius: 50%;
    background: var(--brand-red);
    flex: none;
  }
  .brand__name {
    font-weight: 900;
    font-size: 40px;
    color: var(--ink);
    letter-spacing: 1px;
  }

  .card--front .brand {
    position: absolute;
    left: 40px;
    top: 58px;
  }
  .contact {
    position: absolute;
    left: 40px;
    top: 168px;
    list-style: none;
    font-size: 15px;
    color: var(--ink-soft);
    line-height: 1.35;
  }
  .contact__item {
    display: flex;
    align-items: flex-start;
    gap: 9px;
    margin-bottom: 3px;
  }
  .contact__icon {
    width: 17px;
    height: 17px;
    flex: none;
    margin-top: 1px;
  }

  .card--back .details {
    position: absolute;
    right: 34px;
    top: 96px;
    display: flex;
    flex-direction: column;
    align-items: flex-end;
  }
  .hours {
    margin-top: 18px;
    font-weight: 900;
    font-size: 24px;
    color: var(--brand-red);
  }
  .closed {
    margin-top: 4px;
    font-size: 13px;
    font-weight: 500;
    color: var(--ink);
  }
</style>
</head>
<body>

  <section class="card card--back">
    <div class="halftone halftone--back" role="img" aria-label="Red halftone dot pattern fading to white"></div>
    <div class="details">
      <div class="brand">
        <span class="brand__dot"></span>
        <span class="brand__name">Tindlebox</span>
      </div>
      <p class="hours">M-F 10AM-4PM</p>
      <p class="closed">Sat and Sunday Closed</p>
    </div>
  </section>

  <section class="card card--front">
    <div class="halftone halftone--front" role="img" aria-label="Red halftone dot pattern fading to white"></div>
    <div class="brand">
      <span class="brand__dot"></span>
      <span class="brand__name">Tindlebox</span>
    </div>
    <ul class="contact">
      <li class="contact__item">
        <svg class="contact__icon" viewBox="0 0 20 20" aria-hidden="true">
          <circle cx="10" cy="10" r="10" fill="var(--brand-red)"/>
          <path d="M7 5.2l1.6-.4 1.2 2.6-1 .9c.5 1.2 1.4 2.1 2.6 2.6l.9-1 2.6 1.2-.4 1.6c-.2.6-.8 1-1.4.9C10 13.2 6.8 10 6.4 6.6c-.1-.6.3-1.2.6-1.4z" fill="#fff"/>
        </svg>
        <span>9094417382</span>
      </li>
      <li class="contact__item">
        <svg class="contact__icon" viewBox="0 0 20 20" aria-hidden="true">
          <circle cx="10" cy="10" r="10" fill="var(--brand-red)"/>
          <g fill="none" stroke="#fff" stroke-width="1.2">
            <circle cx="10" cy="10" r="5"/>
            <ellipse cx="10" cy="10" rx="2.2" ry="5"/>
            <path d="M5 10h10"/>
          </g>
        </svg>
        <span>Tindlebox.com</span>
      </li>
      <li class="contact__item">
        <svg class="contact__icon" viewBox="0 0 20 20" aria-hidden="true">
          <circle cx="10" cy="10" r="10" fill="var(--brand-red)"/>
          <path d="M10 4.5a3.6 3.6 0 0 0-3.6 3.6c0 2.7 3.6 7 3.6 7s3.6-4.3 3.6-7A3.6 3.6 0 0 0 10 4.5z" fill="#fff"/>
          <circle cx="10" cy="8.1" r="1.3" fill="var(--brand-red)"/>
        </svg>
        <span>457 Calloway Court Suite B<br>Fernvale CA 92417</span>
      </li>
    </ul>
  </section>

</body>
</html>
```